Website re-design

We are a successful furnished apartment provider in Boston. We currently are working on re-designing our website www.ribtenlofts.com to make it more modern, designer look and user friendly. We hired a designer, but are not happy with the designs proposed and want to improve on them. The winning design will be paid regardless of whether we stay with our current designer or not. We want ideas and functional page links to see how it will work. Platform we have chosen is wordpress. Feel free to propose others easy for us to update and modify. We do not like Joomla on which website is currently running. We do not like flash nor long load times.
Please use photos on our website for design presentations. www.ribtenlofts.com

Target Market(s)

doctors, nurses, business men but mostly business women, some post-medical students

Industry/Entity Type

Apartment

Requirements
Must have
• Quick action button for reservation form and a notification and email forwarding system to us of reservation information by potential clients. Blog required with feedback by guests allowed, we can censor which are published. Slide shows of apartments.
Should not have
• No movies.

```html
<!DOCTYPE html>
<html lang="en">
<head>
<meta charset="utf-8">
<title>Ribten Lofts – Furnished Apartments</title>
<link rel="stylesheet" href="https://fonts.googleapis.com/css2?family=Open+Sans:wght@400;600;700&family=Oswald:wght@400&display=swap">
<style>
:root{
  --dark:#232323;
  --dark-2:#2d2d2d;
  --floor:#dcdcdc;
  --page:#efefef;
  --orange-top:#f27a1e;
  --orange-bottom:#d8430a;
  --orange-text:#f28a1c;
  --gold:#c9ae72;
  --ribbon:#4b4541;
  --ribbon-dark:#2f2a27;
  --panel:#ffffff;
  --panel-line:#dddddd;
  --text:#3a3a3a;
  --muted:#555555;
  --link:#c5470e;
  --btn:#4c4541;
  --btn-blue:#4f6470;
  --footer:#262626;
  --footer-text:#9a9a9a;
}
*{box-sizing:border-box;margin:0;padding:0}
html,body{width:1000px;height:1200px;overflow:hidden}
body{
  position:relative;
  font-family:"Open Sans",Arial,sans-serif;
  color:var(--text);
  background:linear-gradient(to bottom,var(--dark) 0,var(--dark-2) 410px,#8c8c8c 416px,var(--floor) 470px,var(--page) 560px,var(--page) 100%);
}
.stripe{position:absolute;left:0;top:0;width:1000px;height:4px;
  background:repeating-linear-gradient(90deg,#e94e3c 0 40px,#f2b43a 40px 80px,#6cc04a 80px 120px,#3aa0d8 120px 160px,#b85cc8 160px 200px)}
.abs{position:absolute}

/* header */
.brand{left:110px;top:22px;display:flex;align-items:center;gap:10px}
.brand-mark{width:50px;height:50px;border-radius:50%;background:var(--gold)}
.brand-name{font-size:28px;font-weight:400;color:var(--gold);letter-spacing:1px}
.reserve-btn{left:660px;top:20px;width:230px;height:58px;background:#1c1c1c;border:1px solid #3a3a3a;
  box-shadow:inset 0 0 0 3px #262626;display:flex;align-items:center;justify-content:center;
  font-family:"Oswald",sans-serif;font-size:21px;color:var(--orange-text);letter-spacing:.5px;text-decoration:none}

/* navigation */
.nav{left:110px;top:93px;width:779px;height:40px;border-radius:3px;
  background:linear-gradient(var(--orange-top),var(--orange-bottom));display:flex;align-items:center;padding-left:18px}
.nav a{color:#fff;font-size:13px;text-decoration:none;text-transform:uppercase;padding:0 18px;height:40px;line-height:40px}
.nav a.active{background:linear-gradient(#6e0b0b,#3d0606);height:46px;margin-top:-6px;line-height:52px;border-radius:3px 3px 0 0;padding:0 9px}

/* slider */
.slider{left:110px;top:144px;width:779px;height:324px;background:#f4f4f4;padding:4px;box-shadow:0 10px 20px rgba(0,0,0,.25)}
.slide{width:100%;height:100%;background:linear-gradient(100deg,#6a4a2a 0%,#d9b98a 25%,#c7915a 50%,#b36c2a 70%,#8a5224 100%)}
.arrow{width:32px;height:32px;border-radius:50%;background:#1d1d1d}
.arrow svg{display:block}

/* panels */
.panel{background:var(--panel);border:1px solid var(--panel-line)}
.ribbon{position:absolute;height:30px;background:var(--ribbon);color:#fff;font-size:15px;display:flex;align-items:center;justify-content:center;
  box-shadow:0 2px 2px rgba(0,0,0,.2)}
.ribbon-tail{position:absolute;top:14px;width:22px;height:26px;background:var(--ribbon-dark)}
.ribbon-tail.l{clip-path:polygon(0 0,100% 0,100% 100%,0 100%,35% 50%)}
.ribbon-tail.r{clip-path:polygon(0 0,100% 0,65% 50%,100% 100%,0 100%)}

.tweets{left:111px;top:503px;width:231px;height:239px}
.tweet{position:absolute;left:20px;width:194px;font-size:9.5px;line-height:13.5px;color:var(--text)}
.tweet a,.tweet .meta{color:var(--link);text-decoration:none}
.sep{position:absolute;left:20px;width:194px;border-top:1px dotted #c8c8c8}
.small-btn{position:absolute;height:14px;border-radius:2px;background:var(--btn-blue);color:#fff;font-size:8.5px;font-weight:700;
  display:flex;align-items:center;justify-content:center;gap:4px;text-decoration:none}

.welcome{left:359px;top:503px;width:530px;height:239px}
.welcome p{position:absolute;left:32px;top:57px;width:470px;font-size:10.5px;line-height:16.6px;color:var(--muted)}
.read-btn{position:absolute;left:32px;top:188px;width:81px;height:26px;background:var(--btn);border-radius:2px;color:#fff;font-size:10px;font-weight:700;
  display:flex;align-items:center;justify-content:center;gap:6px;text-decoration:none}

.blog{left:111px;top:759px;width:231px;height:221px}
.post{position:absolute;left:15px;width:200px;font-size:8.5px;line-height:13px;text-transform:uppercase;color:var(--text)}

/* apartments */
.section-title{left:359px;top:758px;font-size:19px;font-weight:700;color:#333}
.apt{top:786px;width:129px;height:193px;background:#fff;border:1px solid var(--panel-line)}
.apt-photo{position:absolute;left:3px;top:3px;width:121px;height:146px}
.apt-name{position:absolute;left:8px;top:160px;width:115px;font-size:10.5px;font-weight:600;line-height:12px;color:#222}
.apt-foot{position:absolute;left:0;bottom:0;width:100%;height:40px;background:linear-gradient(#fff,#eaeaea)}

/* partners */
.partners{left:110px;top:997px;width:779px;height:112px;background:#ece6d9;border:1px dashed #b9ae96;outline:3px solid #e2dac8}
.partners-title{position:absolute;left:8px;top:37px;font-size:18px;font-weight:700;line-height:18px;color:#2a2a2a}
.badge{position:absolute;top:17px;width:116px;height:78px;background:#fff;border:1px solid #d7d2c6;padding:5px}
.badge span{display:block;width:100%;height:100%}

/* footer */
.footer{left:0;top:1125px;width:1000px;height:75px;background:var(--footer)}
.footer-nav{position:absolute;left:107px;top:13px;display:flex;gap:24px}
.footer-nav a{font-size:10px;color:var(--footer-text);text-decoration:none}
.social-label{position:absolute;left:690px;top:12px;font-size:11.5px;color:#c8c8c8}
.social{position:absolute;top:9px;width:26px;height:26px;border-radius:3px}
.footer-line{position:absolute;left:110px;top:50px;width:779px;border-top:1px dashed #3d3d3d}
.copyright{position:absolute;left:0;top:58px;width:1000px;text-align:center;font-size:8px;color:#6a6a6a;letter-spacing:.3px}
</style>
</head>
<body>
<div class="stripe"></div>

<header>
  <div class="abs brand">
    <span class="brand-mark"></span>
    <span class="brand-name">RIBTEN LOFTS</span>
  </div>
  <a class="abs reserve-btn" href="#reservations">RESERVATION FORM</a>
</header>

<nav class="abs nav">
  <a class="active" href="#">Home</a>
  <a href="#">Apartments</a>
  <a href="#">Reservations</a>
  <a href="#">Blog</a>
  <a href="#">Reviews</a>
  <a href="#">Contact</a>
  <a href="#">Boston</a>
  <a href="#">About Us</a>
</nav>

<section class="abs slider">
  <div class="slide" role="img" aria-label="Slideshow photo of a sunlit furnished studio with bed, desk, dresser and kitchenette"></div>
</section>
<div class="abs arrow" style="left:124px;top:290px"><svg width="32" height="32" viewBox="0 0 32 32"><path d="M19 9l-7 7 7 7" fill="none" stroke="#fff" stroke-width="3"/></svg></div>
<div class="abs arrow" style="left:846px;top:290px"><svg width="32" height="32" viewBox="0 0 32 32"><path d="M13 9l7 7-7 7" fill="none" stroke="#fff" stroke-width="3"/></svg></div>

<aside class="abs panel tweets">
  <span class="ribbon-tail l" style="left:3px"></span>
  <span class="ribbon-tail r" style="left:205px"></span>
  <div class="ribbon" style="left:24px;top:9px;width:180px">LATEST TWEETS</div>
  <div class="tweet" style="top:50px">Dale Harmon on Why You Should Never Listen to Your Customers <a href="#">http://rl.to/Kp4sWq2B</a> via @bizmonthlymag<br><span class="meta">4 day(s) ago from Post Button</span></div>
  <div class="sep" style="top:108px"></div>
  <div class="tweet" style="top:116px">I posted a new photo to Friendbook<br><a href="#">http://rl.to/hT7mYx3d</a><br><span class="meta">5 day(s) ago from Friendbook</span></div>
  <div class="sep" style="top:161px"></div>
  <div class="tweet" style="top:169px">Design and decor evolution at Ribten Lofts<br><a href="#">http://rl.to/Zc9nQe1v</a><br><span class="meta">5 day(s) ago from Friendbook</span></div>
  <a class="small-btn" href="#" style="left:104px;top:215px;width:110px">Follow me on Chirper <svg width="7" height="6" viewBox="0 0 7 6"><path d="M0 3h6M4 1l2 2-2 2" fill="none" stroke="#fff"/></svg></a>
</aside>

<main>
  <section class="abs panel welcome">
    <span class="ribbon-tail l" style="left:3px"></span>
    <span class="ribbon-tail r" style="left:503px"></span>
    <div class="ribbon" style="left:24px;top:7px;width:480px;height:32px;font-size:17.5px">Welcome to&nbsp;<b>Ribten Lofts Furnished Apartments</b></div>
    <p>Ribten Lofts is proud to offer some of the best furnished apartments in Boston. Our locations are in the trendiest area of the city: the South End. In the South End neighborhood, you will find wonderful restaurants, theaters, cafes and artist lofts. Our short term and extended stay apartments are very, very clean. We also offer the latest designer layouts: hardwood floors, Wireless Dsl, Cable TV, flat screen in most apartments, washer and dryer, cookware, cotton linens. Please click links on left for photo galleries, pricing, availability and reservation form and write us for more information. Thank you.</p>
    <a class="read-btn" href="#">Read More <svg width="7" height="6" viewBox="0 0 7 6"><path d="M0 3h6M4 1l2 2-2 2" fill="none" stroke="#fff"/></svg></a>
  </section>

  <h2 class="abs section-title">APARTMENTS</h2>
  <article class="abs apt" style="left:359px"><div class="apt-foot"></div><div class="apt-photo" role="img" aria-label="Photo of Deluxe Apartment T5 bedroom" style="background:linear-gradient(160deg,#e8c89a,#b98a55)"></div><div class="apt-name">Deluxe Apartment T5</div></article>
  <article class="abs apt" style="left:493px"><div class="apt-foot"></div><div class="apt-photo" role="img" aria-label="Photo of Extended stay Apartment W11 bedroom" style="background:linear-gradient(160deg,#d8c27a,#7d6040)"></div><div class="apt-name">Extended stay Apartment W11</div></article>
  <article class="abs apt" style="left:626px"><div class="apt-foot"></div><div class="apt-photo" role="img" aria-label="Photo of Bohemian apartment W13 living area" style="background:linear-gradient(160deg,#ece6da,#8a6a4a)"></div><div class="apt-name">Bohemian apartment W13</div></article>
  <article class="abs apt" style="left:759px"><div class="apt-foot"></div><div class="apt-photo" role="img" aria-label="Photo of Extended stay Apartment W12 living room" style="background:linear-gradient(160deg,#d9c074,#6a5a48)"></div><div class="apt-name">Extended stay Apartment W12</div></article>
</main>

<aside class="abs panel blog">
  <span class="ribbon-tail l" style="left:3px"></span>
  <span class="ribbon-tail r" style="left:205px"></span>
  <div class="ribbon" style="left:24px;top:8px;width:180px">OUR BLOG</div>
  <div class="post" style="top:59px">Corporate apartment design evolution<br>Tuesday, 10 January 2012 21:27</div>
  <div class="sep" style="top:89px;left:15px;width:200px"></div>
  <div class="post" style="top:95px">Corporate housing Boston - Ribten Lofts<br>Tuesday, 10 January 2012 21:27</div>
  <div class="sep" style="top:126px;left:15px;width:200px"></div>
  <div class="post" style="top:131px">Pumpkin morning in Yarmouth, MA - Ribten Lofts<br>Thursday, 27 October 2011 14:48</div>
  <a class="small-btn" href="#" style="left:153px;top:187px;width:61px">Read More <svg width="7" height="6" viewBox="0 0 7 6"><path d="M0 3h6M4 1l2 2-2 2" fill="none" stroke="#fff"/></svg></a>
</aside>

<section class="abs partners">
  <div class="partners-title">OUR LINK<br>PARTNERS</div>
  <div class="badge" style="left:114px"><span style="background:#5a4d45"></span></div>
  <div class="badge" style="left:245px"><span style="background:#e9eef2"></span></div>
  <div class="badge" style="left:379px"><span style="background:#f0f0f0"></span></div>
  <div class="badge" style="left:511px"><span style="background:#eef3f8"></span></div>
  <div class="badge" style="left:644px"><span style="background:#d9d9b8"></span></div>
</section>

<footer class="abs footer">
  <nav class="footer-nav">
    <a href="#">Home</a><a href="#">Apartments</a><a href="#">Reservations</a><a href="#">Blog</a><a href="#">Reviews</a><a href="#">Contact</a><a href="#">Boston</a><a href="#">About Us</a>
  </nav>
  <span class="social-label">We Are Social</span>
  <span class="social" style="left:773px;background:#3b5a98"></span>
  <span class="social" style="left:803px;background:#3ab0e2"></span>
  <span class="social" style="left:833px;background:#5a9a3a"></span>
  <span class="social" style="left:864px;background:#d9261c"><svg width="26" height="26" viewBox="0 0 26 26"><rect x="6" y="8" width="14" height="10" fill="none" stroke="#fff" stroke-width="1.6"/><path d="M6 8l7 6 7-6" fill="none" stroke="#fff" stroke-width="1.6"/></svg></span>
  <div class="footer-line"></div>
  <div class="copyright">© 2012 RIBTEN LOFTS 2010 - ALL RIGHTS RESERVED</div>
</footer>
</body>
</html>
```